Talon Microchips PowerPoint Master Slide Deck Design

This is a 2-phase project to design a slide deck for a semiconductor company in the Silicon Valley. The design budget will be increased with each phase.
The slide deck will need to have one version with a dark background for presentations and a second version with a white background. Otherwise, the slides will be the same. I anticipate we will need a total of 10 slides, but that number may change.
The first phase will be to design a Title and a Title and Content slide.
- The Title Slide is the first slide of the deck. It should include the presentation title, the presenter's name and date of presentation
- The Title and Content slide should include a title and content with bullet points and up to 2 additional sub-bullets
- The Title and Content slide should have a footer that includes the slide #, Talon Microchips Confidential, and the logo. This footer will be on every slide except the Title Slide
The first two slides will serve as the format for the remaining ~8 slides:
-Header and Content Text (1, 2, 4 column)
-Header and Content Image (bar chart, pie chart, tables)
-Break
-Title only
-Closing (Talon logo only)
Our slides contain a lot of content so a clean and simple design is best.
Both phases will need to include pre-set color options for
-Text and Lines
-Shadows
-Bullets and sub-bullets (including shapes, ex. circle, slash, square, etc.)
-Bar charts, pie charts, tables
Samples of our collateral are attached. Logo files are also attached

```html
<!DOCTYPE html>
<html lang="en">
<head>
<meta charset="utf-8">
<title>Talon Microchips – Master Slide Deck</title>
<link href="https://fonts.googleapis.com/css2?family=Poppins:ital,wght@0,300;0,400;0,500;0,600;0,700;1,400&display=swap" rel="stylesheet">
<style>
  :root {
    --ink: #2b2b2b;
    --stage: #000000;
    --white: #ffffff;
    --blue-deep: #1f4ff2;
    --blue-mid: #1a73f7;
    --cyan: #2ad3fb;
    --ring-pale: #d3f2fc;
    --wash-lilac: #dfe3fb;
    --wash-cyan: #e4f6fd;
    --link-grey: #c9d0dc;
  }
  * { box-sizing: border-box; margin: 0; padding: 0; }
  html, body { width: 1200px; height: 1000px; overflow: hidden; background: var(--stage); }
  body { font-family: 'Poppins', sans-serif; color: var(--ink); position: relative; }

  .slide { position: absolute; width: 325px; height: 231px; background: var(--white); overflow: hidden; }
  .slide .backdrop { position: absolute; inset: 0; width: 100%; height: 100%; }
  .slide .content { position: absolute; inset: 0; }

  .row-1 { top: 101px; } .row-2 { top: 348px; } .row-3 { top: 599px; }
  .col-1 { left: 96px; } .col-2 { left: 437px; } .col-3 { left: 779px; }

  /* footer */
  .footer {
    position: absolute; left: 0; right: 0; bottom: 0; height: 37px;
    background: linear-gradient(90deg, var(--blue-deep) 0%, #3a7cf7 60%, var(--cyan) 100%);
  }
  .footer .brand {
    position: absolute; left: 12px; top: 12px; display: flex; align-items: center; gap: 5px;
    color: var(--white); font-size: 10px; font-weight: 500; letter-spacing: .3px;
  }
  .footer .brand .mark { width: 8px; height: 8px; border-radius: 50%; background: var(--white); }
  .footer .divider { position: absolute; left: 85px; top: 6px; width: 1px; height: 26px; background: var(--white); }
  .footer .confidential {
    position: absolute; left: 95px; bottom: 5px; color: var(--white);
    font-size: 12.4px; font-weight: 700; white-space: nowrap;
  }
  .footer .slide-no {
    position: absolute; right: 28px; top: 3px; width: 62px; height: 13px; border-radius: 7px;
    background: var(--white); color: var(--ink); font-size: 8.5px; font-style: italic;
    text-align: center; line-height: 13px;
  }

  /* title slide */
  .cover .kicker { position: absolute; left: 22px; top: 33px; font-size: 17px; font-weight: 400; }
  .cover .title { position: absolute; left: 22px; top: 53px; font-size: 29px; font-weight: 700; letter-spacing: -.3px; }
  .cover .presenter { position: absolute; left: 73px; top: 95px; font-size: 11.5px; font-weight: 400; }
  .cover .date {
    position: absolute; left: 73px; top: 122px; padding: 1px 8px; border-radius: 9px;
    background: linear-gradient(90deg, var(--cyan), var(--blue-mid)); color: var(--white);
    font-size: 8.5px; letter-spacing: .6px;
  }

  /* title & content */
  .deck-title { position: absolute; left: 29px; top: 24px; font-size: 27px; font-weight: 700; letter-spacing: -.2px; white-space: nowrap; }
  .lede { position: absolute; left: 32px; top: 60px; width: 215px; font-size: 6.6px; line-height: 1.25; text-align: justify; }
  .bullet { position: absolute; left: 34px; top: 88px; display: flex; align-items: center; gap: 6px; font-size: 13.5px; font-weight: 600; }
  .sub { position: absolute; left: 57px; display: flex; align-items: center; gap: 7px; font-size: 10px; }
  .sub.one { top: 119px; } .sub.two { top: 140px; }

  /* columns slide */
  .header { position: absolute; font-size: 20px; font-weight: 700; white-space: nowrap; }
  .columns .header { left: 0; right: 0; top: 20px; text-align: center; }
  .columns .link { position: absolute; left: 50px; top: 78px; width: 230px; height: 18px; background: var(--link-grey); }
  .pill {
    position: absolute; top: 57px; width: 61px; height: 120px; border-radius: 31px;
    background: linear-gradient(180deg, #4aa3fa 0%, #2d63f2 70%, #1f3ff0 100%);
  }
  .pill .head {
    position: absolute; left: 2px; top: 1px; width: 57px; height: 57px; border-radius: 50%;
    background: radial-gradient(circle at 50% 30%, #12c6fb 0%, #1b6ef6 60%, #1d3fef 100%);
    color: var(--white); font-size: 8.6px; font-weight: 600; display: flex; align-items: center; justify-content: center;
  }
  .pill .label { position: absolute; top: 60px; left: 0; right: 0; text-align: center; color: var(--white); font-size: 5.6px; font-weight: 600; }
  .pill .text { position: absolute; top: 68px; left: 6px; right: 6px; text-align: center; color: var(--white); font-size: 5.1px; line-height: 1.45; font-weight: 300; }

  /* chart slide */
  .chart .header { left: 143px; top: 21px; font-size: 18.5px; }
  .chart .lede { left: 146px; top: 49px; width: 175px; text-align: left; font-size: 6.2px; }
  .chart .photo { position: absolute; left: -40px; top: 9px; width: 185px; height: 185px; border-radius: 50%;
    background: radial-gradient(circle at 35% 45%, #b9c6d6 0%, #5d7fb8 30%, #1f4ff2 70%, #0e2a9c 100%); }
  .chart .caption { position: absolute; left: 187px; top: 161px; font-size: 6.2px; font-weight: 600; }
  .chart .caption-text { position: absolute; left: 187px; top: 170px; width: 95px; font-size: 3.4px; line-height: 1.4; }

  /* centered titles */
  .big-title { position: absolute; left: 0; right: 0; top: 78px; text-align: center; font-size: 29px; font-weight: 700; letter-spacing: -.2px; white-space: nowrap; }
  .section-bar { position: absolute; left: 46px; top: 46px; width: 3px; height: 76px; background: linear-gradient(180deg, var(--blue-deep), var(--cyan)); }
  .section-text { position: absolute; left: 57px; top: 55px; font-size: 27px; font-weight: 700; line-height: 1; letter-spacing: .2px; }

  /* closing */
  .closing .brand-lockup { position: absolute; left: 18px; top: 60px; display: flex; align-items: center; gap: 10px; }
  .closing .brand-lockup .mark { width: 22px; height: 22px; border-radius: 50%; background: var(--blue-deep); }
  .closing .brand-lockup .name { font-size: 23px; font-weight: 500; color: var(--ink); white-space: nowrap; }
  .closing .thanks { position: absolute; left: 255px; top: 164px; font-size: 7px; font-weight: 700; }
  .closing .thanks-text { position: absolute; left: 255px; top: 173px; width: 48px; font-size: 2.6px; line-height: 1.4; }

  .note {
    position: absolute; left: 0; right: 0; top: 850px; text-align: center;
    color: var(--white); font-size: 29px; font-style: italic; font-weight: 300; letter-spacing: 3px;
  }
</style>
</head>
<body>

<svg width="0" height="0" style="position:absolute">
  <defs>
    <linearGradient id="wash" x1="0" y1="1" x2="1" y2="0">
      <stop offset="0" stop-color="#dde1fb"/><stop offset="1" stop-color="#e6f8fd"/>
    </linearGradient>
    <linearGradient id="ring" x1="0" y1="1" x2="1" y2="0">
      <stop offset="0" stop-color="#e0e6fb"/><stop offset="1" stop-color="#cdf1fc"/>
    </linearGradient>
    <linearGradient id="coverRing" x1="0" y1="1" x2="1" y2="0">
      <stop offset="0" stop-color="#1f55f3"/><stop offset=".55" stop-color="#0b8ef8"/><stop offset="1" stop-color="#00d2fd"/>
    </linearGradient>
    <linearGradient id="bar" x1="0" y1="0" x2="0" y2="1">
      <stop offset="0" stop-color="#1f3ff0"/><stop offset="1" stop-color="#15b8fb"/>
    </linearGradient>
    <g id="backdrop">
      <rect width="325" height="231" fill="url(#wash)"/>
      <circle cx="218" cy="32" r="178" fill="url(#ring)"/>
      <circle cx="160" cy="22" r="150" fill="#ffffff"/>
    </g>
  </defs>
</svg>

<!-- Title slide -->
<section class="slide cover row-1 col-1">
  <svg class="backdrop" viewBox="0 0 325 231">
    <circle cx="95" cy="0" r="215" fill="url(#coverRing)"/>
    <circle cx="95" cy="0" r="170" fill="#ffffff"/>
  </svg>
  <div class="content">
    <p class="kicker">write here</p>
    <h1 class="title">Presentation</h1>
    <p class="presenter">presenter's name</p>
    <p class="date">12.12.2023</p>
  </div>
</section>

<!-- Title and content -->
<section class="slide row-1 col-2">
  <svg class="backdrop" viewBox="0 0 325 231"><use href="#backdrop"/></svg>
  <div class="content">
    <h2 class="deck-title">Write title here</h2>
    <p class="lede">Lorem ipsum dolor sit amet, consectetuer adipiscing elit, sed diam nonummy nibh euismod tincidunt</p>
    <p class="bullet">
      <svg width="15" height="15" viewBox="0 0 15 15"><path d="M2 7.5h7M6 2.5l5 5-5 5" fill="none" stroke="#1a73f7" stroke-width="2.6" stroke-linecap="round" stroke-linejoin="round"/></svg>
      Write bullete here
    </p>
    <p class="sub one"><svg width="10" height="10" viewBox="0 0 10 10"><circle cx="5" cy="5" r="5" fill="#1a73f7"/><path d="M3 5h3.5M5 3l2 2-2 2" fill="none" stroke="#fff" stroke-width="1.2"/></svg>Write sub-bullets here</p>
    <p class="sub two"><svg width="10" height="10" viewBox="0 0 10 10"><circle cx="5" cy="5" r="5" fill="#1a73f7"/><path d="M3 5h3.5M5 3l2 2-2 2" fill="none" stroke="#fff" stroke-width="1.2"/></svg>Write sub-bullets here</p>
  </div>
  <footer class="footer"><span class="brand"><span class="mark"></span>TALON</span><span class="divider"></span><span class="slide-no">Slide #1</span><span class="confidential">Talon Microchips Confidential</span></footer>
</section>

<!-- Four columns -->
<section class="slide columns row-1 col-3">
  <svg class="backdrop" viewBox="0 0 325 231"><use href="#backdrop"/></svg>
  <div class="content">
    <h2 class="header">Write header here</h2>
    <div class="link"></div>
    <div class="pill" style="left:27px"><div class="head">Column 1</div><p class="label">LOREM IPSUM</p><p class="text">Lorem ipsum is simply dummy text of the printing and typesetting industry magan.</p></div>
    <div class="pill" style="left:98px"><div class="head">Column 2</div><p class="label">LOREM IPSUM</p><p class="text">Lorem ipsum is simply dummy text of the printing and typesetting industry magan.</p></div>
    <div class="pill" style="left:170px"><div class="head">Column 3</div><p class="label">LOREM IPSUM</p><p class="text">Lorem ipsum is simply dummy text of the printing and typesetting industry magan.</p></div>
    <div class="pill" style="left:241px"><div class="head">Column 4</div><p class="label">LOREM IPSUM</p><p class="text">Lorem ipsum is simply dummy text of the printing and typesetting industry magan.</p></div>
  </div>
  <footer class="footer"><span class="brand"><span class="mark"></span>TALON</span><span class="divider"></span><span class="slide-no">Slide #2</span><span class="confidential">Talon Microchips Confidential</span></footer>
</section>

<!-- Header, image and chart -->
<section class="slide chart row-2 col-1">
  <svg class="backdrop" viewBox="0 0 325 231"><use href="#backdrop"/></svg>
  <div class="content">
    <div class="photo" role="img" aria-label="Close-up photo of a microchip on a blue circuit board"></div>
    <h2 class="header">Write header here</h2>
    <p class="lede">Lorem ipsum dolor sit amet, consectetuer adipiscing elit, sed diam nonummy nibh euismod tincidunt</p>
    <svg style="position:absolute;left:185px;top:70px" width="110" height="88" viewBox="0 0 110 88" font-family="Poppins, sans-serif" font-size="5" font-weight="600" fill="#2b2b2b">
      <line x1="2" y1="0" x2="2" y2="86" stroke="#1a73f7" stroke-width="1"/>
      <line x1="2" y1="86" x2="102" y2="86" stroke="#1a73f7" stroke-width="1"/>
      <rect x="6" y="27" width="10" height="59" fill="url(#bar)"/><text x="5" y="22">0,01</text>
      <rect x="20" y="21" width="10" height="65" fill="url(#bar)"/><text x="19" y="16">0,05</text>
      <rect x="34" y="44" width="10" height="42" fill="url(#bar)"/><text x="33" y="39">0,36</text>
      <rect x="48" y="15" width="10" height="71" fill="url(#bar)"/><text x="47" y="10">0,15</text>
      <rect x="62" y="48" width="10" height="38" fill="url(#bar)"/><text x="61" y="43">0,17</text>
      <rect x="76" y="37" width="10" height="49" fill="url(#bar)"/><text x="75" y="32">0,09</text>
      <rect x="90" y="56" width="10" height="30" fill="url(#bar)"/><text x="89" y="51">0,23</text>
    </svg>
    <p class="caption">LOREM IPSUM</p>
    <p class="caption-text">Lorem ipsum is simply dummy text of the printing and typesetting industry.</p>
  </div>
  <footer class="footer"><span class="brand"><span class="mark"></span>TALON</span><span class="divider"></span><span class="slide-no">Slide #3</span><span class="confidential">Talon Microchips Confidential</span></footer>
</section>

<!-- Section break -->
<section class="slide row-2 col-2">
  <svg class="backdrop" viewBox="0 0 325 231"><use href="#backdrop"/></svg>
  <div class="content">
    <span class="section-bar"></span>
    <h2 class="section-text">SECTION<br>BREAK</h2>
  </div>
  <footer class="footer"><span class="brand"><span class="mark"></span>TALON</span><span class="divider"></span><span class="slide-no">Slide #4</span><span class="confidential">Talon Microchips Confidential</span></footer>
</section>

<!-- Title only -->
<section class="slide row-2 col-3">
  <svg class="backdrop" viewBox="0 0 325 231"><use href="#backdrop"/></svg>
  <div class="content"><h2 class="big-title">write your Title</h2></div>
  <footer class="footer"><span class="brand"><span class="mark"></span>TALON</span><span class="divider"></span><span class="slide-no">Slide #5</span><span class="confidential">Talon Microchips Confidential</span></footer>
</section>

<section class="slide row-3 col-1">
  <svg class="backdrop" viewBox="0 0 325 231"><use href="#backdrop"/></svg>
  <div class="content"><h2 class="big-title">write your Title 2</h2></div>
  <footer class="footer"><span class="brand"><span class="mark"></span>TALON</span><span class="divider"></span><span class="slide-no">Slide #6</span><span class="confidential">Talon Microchips Confidential</span></footer>
</section>

<section class="slide row-3 col-2">
  <svg class="backdrop" viewBox="0 0 325 231"><use href="#backdrop"/></svg>
  <div class="content"><h2 class="big-title">write your Title 3</h2></div>
  <footer class="footer"><span class="brand"><span class="mark"></span>TALON</span><span class="divider"></span><span class="slide-no">Slide #7</span><span class="confidential">Talon Microchips Confidential</span></footer>
</section>

<!-- Closing -->
<section class="slide closing row-3 col-3">
  <svg class="backdrop" viewBox="0 0 325 231"><use href="#backdrop"/></svg>
  <div class="content">
    <div class="brand-lockup"><span class="mark"></span><span class="name">Talon Microchips</span></div>
    <p class="thanks">THANK YOU!</p>
    <p class="thanks-text">Lorem ipsum is simply dummy text of the printing and typesetting industry.</p>
  </div>
  <footer class="footer"><span class="brand"><span class="mark"></span>TALON</span><span class="divider"></span><span class="slide-no">Slide #8</span><span class="confidential">Talon Microchips Confidential</span></footer>
</section>

<p class="note">{hope you like this.... waiting your feedback}</p>

</body>
</html>
```